Lume Hart Co Need a custom graphic

I need to have the attached chart re-designed in a hand colored pencil format. The heading needs to be changed to "The most effective methods for hiring sales people". Do not include the background logo in the sample file.

Place the attached Lume Hart Co logo next to the most effective methods (91%)

```html
<!DOCTYPE html>
<html lang="en">
<head>
<meta charset="utf-8">
<title>The Most Effective Methods for Hiring Sales People</title>
<link rel="stylesheet" href="https://fonts.googleapis.com/css2?family=Amatic+SC:wght@400;700&family=Cabin+Sketch:wght@400;700&display=swap">
<style>
  :root {
    --paper: #ffffff;
    --grid: #d9d9d9;
    --purple: #4b0082;
    --violet: #2a10c8;
    --blue: #0a0aff;
    --navy: #1f3f7f;
    --green: #0a7f0a;
    --lime: #7fbf00;
    --olive: #c8c800;
    --gold: #f2c800;
    --orange: #ffa500;
    --orange-red: #ff4f00;
    --red: #f01010;
  }
  html, body {
    margin: 0;
    padding: 0;
    width: 1200px;
    height: 848px;
    overflow: hidden;
    background: var(--paper);
  }
  .chart { display: block; width: 1200px; height: 848px; }
  .title-band { fill: var(--purple); }
  .title-text {
    font-family: "Cabin Sketch", "Amatic SC", cursive;
    font-size: 78px;
    fill: #ffffff;
  }
  .grid line { stroke: var(--grid); stroke-width: 1.5; }
  .tick-label {
    font-family: "Amatic SC", cursive;
    font-weight: 700;
    font-size: 52px;
    fill: var(--purple);
  }
  .axis-title {
    font-family: "Cabin Sketch", cursive;
    font-size: 72px;
    fill: var(--purple);
  }
  .callout rect { fill: none; stroke-width: 2.2; }
  .callout text {
    font-family: "Amatic SC", cursive;
    font-weight: 700;
    font-size: 38px;
  }
  .callout path { fill: none; stroke-width: 2.2; }
  .segment { stroke-width: 4.5; stroke-linecap: round; fill: none; }
  .brand-name {
    font-family: "Amatic SC", cursive;
    font-weight: 700;
    font-size: 38px;
    fill: var(--navy);
  }
</style>
</head>
<body>
<svg class="chart" viewBox="0 0 2280 1611" xmlns="http://www.w3.org/2000/svg" role="img" aria-label="Line chart of predictive validity by hiring method for sales people">
  <defs>
    <marker id="tip-red" viewBox="0 0 10 10" refX="9" refY="5" markerWidth="9" markerHeight="9" orient="auto"><path d="M0 0 L10 5 L0 10 L3 5 Z" fill="var(--red)"/></marker>
    <marker id="tip-orange-red" viewBox="0 0 10 10" refX="9" refY="5" markerWidth="9" markerHeight="9" orient="auto"><path d="M0 0 L10 5 L0 10 L3 5 Z" fill="var(--orange-red)"/></marker>
    <marker id="tip-orange" viewBox="0 0 10 10" refX="9" refY="5" markerWidth="9" markerHeight="9" orient="auto"><path d="M0 0 L10 5 L0 10 L3 5 Z" fill="var(--orange)"/></marker>
    <marker id="tip-gold" viewBox="0 0 10 10" refX="9" refY="5" markerWidth="9" markerHeight="9" orient="auto"><path d="M0 0 L10 5 L0 10 L3 5 Z" fill="var(--gold)"/></marker>
    <marker id="tip-olive" viewBox="0 0 10 10" refX="9" refY="5" markerWidth="9" markerHeight="9" orient="auto"><path d="M0 0 L10 5 L0 10 L3 5 Z" fill="var(--olive)"/></marker>
    <marker id="tip-lime" viewBox="0 0 10 10" refX="9" refY="5" markerWidth="9" markerHeight="9" orient="auto"><path d="M0 0 L10 5 L0 10 L3 5 Z" fill="var(--lime)"/></marker>
    <marker id="tip-green" viewBox="0 0 10 10" refX="9" refY="5" markerWidth="9" markerHeight="9" orient="auto"><path d="M0 0 L10 5 L0 10 L3 5 Z" fill="var(--green)"/></marker>
    <marker id="tip-navy" viewBox="0 0 10 10" refX="9" refY="5" markerWidth="9" markerHeight="9" orient="auto"><path d="M0 0 L10 5 L0 10 L3 5 Z" fill="var(--navy)"/></marker>
    <marker id="tip-blue" viewBox="0 0 10 10" refX="9" refY="5" markerWidth="9" markerHeight="9" orient="auto"><path d="M0 0 L10 5 L0 10 L3 5 Z" fill="var(--blue)"/></marker>
    <marker id="tip-violet" viewBox="0 0 10 10" refX="9" refY="5" markerWidth="9" markerHeight="9" orient="auto"><path d="M0 0 L10 5 L0 10 L3 5 Z" fill="var(--violet)"/></marker>
    <marker id="tip-purple" viewBox="0 0 10 10" refX="9" refY="5" markerWidth="9" markerHeight="9" orient="auto"><path d="M0 0 L10 5 L0 10 L3 5 Z" fill="var(--purple)"/></marker>
  </defs>

  <!-- Title band -->
  <rect class="title-band" x="343" y="148" width="1784" height="125"/>
  <text class="title-text" x="400" y="236" textLength="1648" lengthAdjust="spacingAndGlyphs">THE MOST EFFECTIVE METHODS FOR HIRING SALES PEOPLE</text>

  <!-- Grid -->
  <g class="grid">
    <line x1="343" y1="273" x2="343" y2="1404"/>
    <line x1="505" y1="273" x2="505" y2="1404"/>
    <line x1="667" y1="273" x2="667" y2="1404"/>
    <line x1="829" y1="273" x2="829" y2="1404"/>
    <line x1="991" y1="273" x2="991" y2="1404"/>
    <line x1="1154" y1="273" x2="1154" y2="1404"/>
    <line x1="1316" y1="273" x2="1316" y2="1404"/>
    <line x1="1478" y1="273" x2="1478" y2="1404"/>
    <line x1="1640" y1="273" x2="1640" y2="1404"/>
    <line x1="1803" y1="273" x2="1803" y2="1404"/>
    <line x1="1965" y1="273" x2="1965" y2="1404"/>
    <line x1="2127" y1="273" x2="2127" y2="1404"/>
    <line x1="343" y1="398" x2="2127" y2="398"/>
    <line x1="343" y1="524" x2="2127" y2="524"/>
    <line x1="343" y1="650" x2="2127" y2="650"/>
    <line x1="343" y1="776" x2="2127" y2="776"/>
    <line x1="343" y1="901" x2="2127" y2="901"/>
    <line x1="343" y1="1027" x2="2127" y2="1027"/>
    <line x1="343" y1="1153" x2="2127" y2="1153"/>
    <line x1="343" y1="1278" x2="2127" y2="1278"/>
    <line x1="343" y1="1404" x2="2127" y2="1404"/>
  </g>

  <!-- Y axis ticks -->
  <g class="ticks">
    <text class="tick-label" x="245" y="328">0.90</text>
    <text class="tick-label" x="245" y="448">0.80</text>
    <text class="tick-label" x="245" y="568">0.70</text>
    <text class="tick-label" x="245" y="688">0.60</text>
    <text class="tick-label" x="245" y="808">0.50</text>
    <text class="tick-label" x="245" y="928">0.40</text>
    <text class="tick-label" x="245" y="1048">0.30</text>
    <text class="tick-label" x="245" y="1168">0.20</text>
    <text class="tick-label" x="245" y="1288">0.10</text>
    <text class="tick-label" x="245" y="1408">0.00</text>
  </g>

  <!-- Axis titles -->
  <text class="axis-title" transform="translate(208 1122) rotate(-90)" textLength="570" lengthAdjust="spacingAndGlyphs">PREDICTIVE VALIDITY</text>
  <text class="axis-title" x="950" y="1475" textLength="395" lengthAdjust="spacingAndGlyphs">HIRING METHOD</text>

  <!-- Data line -->
  <g class="series">
    <line class="segment" x1="509" y1="1308" x2="647" y2="1192" style="stroke:var(--orange-red)"/>
    <line class="segment" x1="647" y1="1192" x2="829" y2="1152" style="stroke:#ff8000"/>
    <line class="segment" x1="829" y1="1152" x2="991" y2="1146" style="stroke:var(--gold)"/>
    <line class="segment" x1="991" y1="1146" x2="1154" y2="1100" style="stroke:var(--olive)"/>
    <line class="segment" x1="1154" y1="1100" x2="1326" y2="1108" style="stroke:#5faa00"/>
    <line class="segment" x1="1326" y1="1108" x2="1478" y2="1003" style="stroke:var(--green)"/>
    <line class="segment" x1="1478" y1="1003" x2="1644" y2="765" style="stroke:#0e5a45"/>
    <line class="segment" x1="1644" y1="765" x2="1805" y2="662" style="stroke:#1030b0"/>
    <line class="segment" x1="1805" y1="662" x2="1967" y2="495" style="stroke:var(--violet)"/>
    <line class="segment" x1="1967" y1="495" x2="2127" y2="301" style="stroke:var(--purple)"/>

    <circle cx="509" cy="1308" r="8" fill="var(--red)"/>
    <circle cx="647" cy="1192" r="8" fill="var(--orange-red)"/>
    <circle cx="829" cy="1152" r="8" fill="var(--orange)"/>
    <circle cx="991" cy="1146" r="8" fill="var(--gold)"/>
    <circle cx="1154" cy="1100" r="8" fill="var(--olive)"/>
    <circle cx="1326" cy="1108" r="8" fill="var(--lime)"/>
    <circle cx="1478" cy="1003" r="8" fill="var(--green)"/>
    <circle cx="1644" cy="765" r="8" fill="var(--navy)"/>
    <circle cx="1805" cy="662" r="8" fill="var(--blue)"/>
    <circle cx="1967" cy="495" r="8" fill="var(--violet)"/>
    <circle cx="2127" cy="301" r="8" fill="var(--purple)"/>
  </g>

  <!-- Callouts -->
  <g class="callout" style="stroke:var(--red);fill:var(--red)">
    <rect x="557" y="1338" width="306" height="57"/>
    <path d="M557 1370 L520 1328" marker-end="url(#tip-red)"/>
    <text x="574" y="1380" stroke="none" textLength="242" lengthAdjust="spacingAndGlyphs">CULTURE TEST, 13%</text>
  </g>
  <g class="callout" style="stroke:var(--orange-red);fill:var(--orange-red)">
    <rect x="385" y="1062" width="306" height="57"/>
    <path d="M592 1120 L636 1173" marker-end="url(#tip-orange-red)"/>
    <text x="447" y="1104" stroke="none" textLength="151" lengthAdjust="spacingAndGlyphs">RESUME, 18%</text>
  </g>
  <g class="callout" style="stroke:var(--orange);fill:var(--orange)">
    <rect x="460" y="984" width="554" height="57"/>
    <path d="M744 1042 L824 1136" marker-end="url(#tip-orange)"/>
    <text x="476" y="1026" stroke="none" textLength="462" lengthAdjust="spacingAndGlyphs">BEHAVIOUR PERSONALITY TEST, 20%</text>
  </g>
  <g class="callout" style="stroke:var(--gold);fill:var(--gold)">
    <rect x="762" y="1228" width="455" height="57"/>
    <path d="M1056 1227 L1003 1164" marker-end="url(#tip-gold)"/>
    <text x="777" y="1270" stroke="none" textLength="380" lengthAdjust="spacingAndGlyphs">TRADITIONAL INTERVIEW, 20%</text>
  </g>
  <g class="callout" style="stroke:var(--olive);fill:var(--olive)">
    <rect x="951" y="907" width="408" height="57"/>
    <path d="M1046 965 L1145 1080" marker-end="url(#tip-olive)"/>
    <text x="985" y="949" stroke="none" textLength="272" lengthAdjust="spacingAndGlyphs">REFERENCE CHECK, 23%</text>
  </g>
  <g class="callout" style="stroke:var(--lime);fill:var(--lime)">
    <rect x="1294" y="1228" width="490" height="57"/>
    <path d="M1420 1227 L1342 1135" marker-end="url(#tip-lime)"/>
    <text x="1314" y="1270" stroke="none" textLength="386" lengthAdjust="spacingAndGlyphs">EMOTIONAL INTELLIGENCE, 23%</text>
  </g>
  <g class="callout" style="stroke:var(--green);fill:var(--green)">
    <rect x="1478" y="1062" width="306" height="57"/>
    <path d="M1530 1061 L1493 1019" marker-end="url(#tip-green)"/>
    <text x="1510" y="1104" stroke="none" textLength="228" lengthAdjust="spacingAndGlyphs">SKILLS TEST, 33%</text>
  </g>
  <g class="callout" style="stroke:var(--navy);fill:var(--navy)">
    <rect x="1019" y="740" width="489" height="57"/>
    <path d="M1509 768 L1618 770" marker-end="url(#tip-navy)"/>
    <text x="1044" y="782" stroke="none" textLength="382" lengthAdjust="spacingAndGlyphs">GENERAL MENTAL ABILITY, 51%</text>
  </g>
  <g class="callout" style="stroke:var(--blue);fill:var(--blue)">
    <rect x="838" y="618" width="822" height="57"/>
    <path d="M1661 650 L1781 655" marker-end="url(#tip-blue)"/>
    <text x="848" y="660" stroke="none" textLength="692" lengthAdjust="spacingAndGlyphs">HIGHLY STRUCTURED INTERVIEW WITH SCORECARD, 57%</text>
  </g>
  <g class="callout" style="stroke:var(--violet);fill:var(--violet)">
    <rect x="1208" y="472" width="609" height="57"/>
    <path d="M1818 497 L1938 496" marker-end="url(#tip-violet)"/>
    <text x="1238" y="514" stroke="none" textLength="494" lengthAdjust="spacingAndGlyphs">MULTI-MEASUREMENT ASSESMENT, 71%</text>
  </g>
  <g class="callout" style="stroke:var(--purple);fill:var(--purple)">
    <rect x="1288" y="310" width="735" height="57"/>
    <path d="M2024 338 L2110 307" marker-end="url(#tip-purple)"/>
    <text x="1310" y="352" stroke="none" textLength="450" lengthAdjust="spacingAndGlyphs">THE MOST EFFECTIVE METHODS, 91%</text>
  </g>
  <text class="brand-name" x="1838" y="352" textLength="160" lengthAdjust="spacingAndGlyphs">LUME HART CO</text>
</svg>
</body>
</html>
```